Cover for a Series of 5 Poetry Books where there is only a subtle (colour?) change for each

I have 5 poetry books to publish all have the main title of Tides Within My Heart then have different subtitles, which are Lone Voyage Past the Coral Straits; Lone Voyage Across Amber Waters, and 3 others I have yet to determine. I have already published the first one and will attach the cover, which needs re-doing for a reprint. I have been given permission to use a photograph of the moon and a universe star pic as I like the idea of using the moon, as it dominates the tides, oceans and weather systems. I like the thought of using the stars because I love to watch them out at sea and the first design of the book I really love, except that I don't have it in 30dpi which is a must. the photo of the boat on the front is a photo of my boat, and I would like to use it too if possible. all that said I am up for some new ideas that you come up with. my poetry is pretty raw at times, but can also be inspiring and I think the book cover needs to reflect this. I am a solo sailor so it has to reflect that too!
I would like the series of 5 books to have covers that are easily recognisable as a series but also are such that people want to pick them up and read. Maybe change the colour of the moon?
I will have a series of 5 books in paperback and e-books printed 6'x9' with approx 116 to 130 pages max I have the back cover info, the photo of the boat and photo of the author. I can get the barcode for the ISBN numbers. I am self-publishing so I do not have a heap of money!
I have had a couple of folk who have kindly reproduced what I already had, that is not what I am looking for. If I am still not clear, please do drop me a line. I am very new to this process.
Thanks
Target Market(s)
Male and female 15 to 35 and 65 to 85
Requirements
Must have
- 5 covers which are clearly slightly different, but recognisable as a series
Should not have
- unhelpful comments - thanks

```html
<!DOCTYPE html>
<html lang="en">
<head>
<meta charset="utf-8">
<title>Tides Within My Heart: Series Covers</title>
<link rel="stylesheet" href="https://fonts.googleapis.com/css2?family=Yellowtail&family=EB+Garamond:ital@1&display=swap">
<style>
  :root {
    --page: #ffffff;
    --night: #050505;
    --ink: #1a1a1a;
    --author: #f4f4f4;
    --foam: #f3ede4;
    --foam-shadow: #c9c3b8;
    --sea-grey: #7f8d8a;
    --sail-light: rgba(246, 246, 244, 0.92);
    --sail-fade: rgba(246, 246, 244, 0);
    --amber-moon: #f6a81c;
    --amber-title: #ef6f1c;
    --amber-base: #f18a1d;
    --gold-moon: #f7e51d;
    --gold-title: #e6b416;
    --gold-base: #f1c21a;
    --crimson-moon: #f0521f;
    --crimson-title: #e8331f;
    --crimson-base: #e8242a;
    --ocean-moon: #2a8ac8;
    --ocean-title: #1b7fc3;
    --ocean-base: #2590d3;
    --lagoon-moon: #22d2bd;
    --lagoon-title: #18a48f;
    --lagoon-base: #20c2c0;
  }
  * { margin: 0; padding: 0; box-sizing: border-box; }
  html, body {
    width: 1134px; height: 1200px; overflow: hidden;
    background: var(--page);
  }
  .series { position: relative; width: 1134px; height: 1200px; }

  .cover {
    position: absolute;
    width: 341px; height: 497px;
    background: var(--night);
    overflow: hidden;
  }
  .cover--amber   { left: 36px;  top: 81px;  --moon: var(--amber-moon);   --title: var(--amber-title);   --base: var(--amber-base); }
  .cover--gold    { left: 405px; top: 80px;  --moon: var(--gold-moon);    --title: var(--gold-title);    --base: var(--gold-base); }
  .cover--crimson { left: 764px; top: 81px;  --moon: var(--crimson-moon); --title: var(--crimson-title); --base: var(--crimson-base); }
  .cover--ocean   { left: 194px; top: 618px; --moon: var(--ocean-moon);   --title: var(--ocean-title);   --base: var(--ocean-base); }
  .cover--lagoon  { left: 610px; top: 618px; --moon: var(--lagoon-moon);  --title: var(--lagoon-title);  --base: var(--lagoon-base); }

  .cover__author {
    position: absolute; top: 26px; left: 0; right: 0;
    text-align: center;
    font-family: "EB Garamond", Georgia, serif;
    font-style: italic;
    font-size: 19px;
    letter-spacing: 0.5px;
    word-spacing: 5px;
    color: var(--author);
  }

  .cover__moon {
    position: absolute;
    left: 48px; top: 63px;
    width: 248px; height: 248px;
    border-radius: 50%;
    background: radial-gradient(circle at 50% 45%, var(--moon) 0%, var(--moon) 40%, color-mix(in srgb, var(--moon) 55%, #000) 100%);
  }

  .cover__surf {
    position: absolute;
    left: 0; right: 0; top: 258px; bottom: 0;
    background: linear-gradient(to bottom,
      rgba(5,5,5,0) 0%,
      var(--sea-grey) 6%,
      var(--foam) 20%,
      var(--foam) 48%,
      var(--foam-shadow) 66%,
      var(--foam) 76%,
      var(--base) 92%,
      var(--base) 100%);
  }

  .cover__boat {
    position: absolute;
    left: 100px; top: 86px;
    width: 150px; height: 200px;
    background: radial-gradient(ellipse at 52% 55%, var(--sail-light) 0%, var(--sail-light) 38%, var(--sail-fade) 72%);
  }

  .cover__title {
    position: absolute;
    left: 0; right: 0; top: 296px;
    font-family: "Yellowtail", "Brush Script MT", cursive;
    font-weight: 400;
    font-size: 46px;
    line-height: 48px;
    color: var(--title);
  }
  .cover__title-line { display: block; white-space: nowrap; }
  .cover__title-line--first  { padding-left: 66px; }
  .cover__title-line--second { padding-left: 48px; }

  .cover__subtitle {
    position: absolute;
    left: 0; right: 0; top: 443px;
    text-align: center;
    font-family: "EB Garamond", Georgia, serif;
    font-style: italic;
    font-size: 18px;
    color: var(--ink);
    white-space: nowrap;
  }
</style>
</head>
<body>
<main class="series">

  <article class="cover cover--amber">
    <p class="cover__author">Maren Ashby</p>
    <div class="cover__moon"></div>
    <div class="cover__surf" role="img" aria-label="Photograph of breaking white surf with a rocky shore"></div>
    <div class="cover__boat" role="img" aria-label="Photograph of the author's sailing yacht under full sail"></div>
    <h1 class="cover__title"><span class="cover__title-line cover__title-line--first">Tides Within</span><span class="cover__title-line cover__title-line--second">My Heart</span></h1>
    <p class="cover__subtitle">Lone Voyage Across Amber Waters</p>
  </article>

  <article class="cover cover--gold">
    <p class="cover__author">Maren Ashby</p>
    <div class="cover__moon"></div>
    <div class="cover__surf" role="img" aria-label="Photograph of breaking white surf with a rocky shore"></div>
    <div class="cover__boat" role="img" aria-label="Photograph of the author's sailing yacht under full sail"></div>
    <h1 class="cover__title"><span class="cover__title-line cover__title-line--first">Tides Within</span><span class="cover__title-line cover__title-line--second">My Heart</span></h1>
    <p class="cover__subtitle">Lone Voyage Past the Coral Straits</p>
  </article>

  <article class="cover cover--crimson">
    <p class="cover__author">Maren Ashby</p>
    <div class="cover__moon"></div>
    <div class="cover__surf" role="img" aria-label="Photograph of breaking white surf with a rocky shore"></div>
    <div class="cover__boat" role="img" aria-label="Photograph of the author's sailing yacht under full sail"></div>
    <h1 class="cover__title"><span class="cover__title-line cover__title-line--first">Tides Within</span><span class="cover__title-line cover__title-line--second">My Heart</span></h1>
    <p class="cover__subtitle">Lone Voyage ..................</p>
  </article>

  <article class="cover cover--ocean">
    <p class="cover__author">Maren Ashby</p>
    <div class="cover__moon"></div>
    <div class="cover__surf" role="img" aria-label="Photograph of breaking white surf with a rocky shore"></div>
    <div class="cover__boat" role="img" aria-label="Photograph of the author's sailing yacht under full sail"></div>
    <h1 class="cover__title"><span class="cover__title-line cover__title-line--first">Tides Within</span><span class="cover__title-line cover__title-line--second">My Heart</span></h1>
    <p class="cover__subtitle">Lone Voyage ..................</p>
  </article>

  <article class="cover cover--lagoon">
    <p class="cover__author">Maren Ashby</p>
    <div class="cover__moon"></div>
    <div class="cover__surf" role="img" aria-label="Photograph of breaking white surf with a rocky shore"></div>
    <div class="cover__boat" role="img" aria-label="Photograph of the author's sailing yacht under full sail"></div>
    <h1 class="cover__title"><span class="cover__title-line cover__title-line--first">Tides Within</span><span class="cover__title-line cover__title-line--second">My Heart</span></h1>
    <p class="cover__subtitle">Lone Voyage ..................</p>
  </article>

</main>
</body>
</html>
```